Zentraly Wordpress Website Update

Over the course of the past two years the website has become bloated and slow. It is at Zentraly.net. The refresh does not need to be an exact copy but should have the same elements of a high technology consulting firm specializing is audio video. The company tag line is "AV Experts in Experiential Design".
The intent is to add a section on the front page that has the "latest news" or selected highlights. As an example the company is underwriting a trade event and we want to list that on there. The pages should be a front page, about, contact, services, and blog.
I have included assets that Zentraly already owns as well as the color templates that were recommended. The overall look thought should be brighter which is why the backgrounds are lighter greens. I have provided all of the assets as I realize that my choices might not have been the best ones.
It is very important that this page be Responsive so that it works on mobile.

Target Market(s)

Theme parks, museums, corporate environments, business to business

Industry/Entity Type

Professional Audio Video

Coding

Font styles to use
Sans Serif
Other font styles liked:
• Raleway & Roboto

Requirements
Must have
• Responsive design. Ability to post news and thoughts, a blog
Nice to have
• I would like to have a design that can also have complimentary

```html
<!DOCTYPE html>
<html lang="en">
<head>
<meta charset="utf-8">
<title>Zentraly – AV Experts in Experiential Design</title>
<link href="https://fonts.googleapis.com/css2?family=Roboto:wght@300;400;500;700&display=swap" rel="stylesheet">
<style>
:root{
  --black:#0b0b0b;
  --footer:#1c1c1c;
  --green:#80de7c;
  --green-dark:#4cc248;
  --green-band:#b7e4b2;
  --green-soft:#d6f4d1;
  --green-pale:#ddfbd8;
  --ink:#111;
  --ink-btn:#16361a;
  --grey:#6b6b6b;
  --white:#fff;
}
*{box-sizing:border-box;margin:0;padding:0}
html,body{width:1200px;height:4326px;overflow:hidden}
body{font-family:'Roboto',sans-serif;color:var(--ink);background:var(--white)}
.page{position:relative;width:1200px;height:4326px;overflow:hidden}
.section{position:absolute;left:0;width:1200px}
.abs{position:absolute}
.btn{position:absolute;display:flex;align-items:center;justify-content:center;gap:10px;height:51px;border-radius:26px;background:var(--green);color:var(--ink-btn);font-weight:700;font-size:15px;letter-spacing:.3px;text-transform:uppercase}
.btn .arrow{width:15px;height:15px;border-radius:50%;background:var(--ink-btn);display:inline-flex;align-items:center;justify-content:center}
.h2{font-size:34px;font-weight:500;color:var(--ink)}
.center{left:0;width:1200px;text-align:center}

/* header */
.site-header{top:0;height:96px;background:var(--black);color:var(--white)}
.brand{left:111px;top:28px;font-size:28px;font-weight:500;line-height:1;color:var(--white)}
.top-contact{top:12px;font-size:14px;display:flex;align-items:center;gap:14px;line-height:28px}
.contact-icon{width:28px;height:28px;border-radius:50%;border:1.5px solid #fff;display:flex;align-items:center;justify-content:center}
.nav{top:63px;font-size:15px;font-weight:700}
.nav a{color:#fff;text-decoration:none;position:absolute;white-space:nowrap}

/* hero */
.hero{top:96px;height:642px;background:linear-gradient(120deg,#2f3352 0%,#403f6b 40%,#272a46 70%,#14172a 100%)}
.hero-title{left:111px;top:139px;font-size:50px;line-height:57px;font-weight:400;color:#fff;width:620px}
.hero-sub{left:111px;top:270px;font-size:20px;line-height:31px;color:#f2f2f2;width:560px}
.hero-dots{top:463px;left:572px;display:flex;gap:4px}
.hero-dots span{width:9px;height:9px;border-radius:50%;background:#fff}
.hero-dots span.off{background:transparent;border:1.5px solid #fff}

/* services cards */
.services{top:738px;height:437px;background:var(--green-band)}
.service-card{position:absolute;top:124px;width:233px;height:229px;background:#fff;border-radius:14px;border:3px solid #e4f6e1;box-shadow:0 4px 10px rgba(0,0,0,.12);text-align:center}
.service-card svg{margin-top:18px}
.service-title{font-size:16px;font-weight:700;margin-top:12px}
.service-rule{width:26px;height:2px;background:var(--green-dark);margin:10px auto 12px}
.service-text{font-size:12.5px;line-height:20px;color:var(--grey);padding:0 16px;text-align:justify;text-align-last:center}

/* feature */
.feature{top:1175px;height:684px;background:#fff}
.feature-block{left:111px;top:85px;width:976px;height:514px;border-radius:44px;overflow:hidden;background:linear-gradient(135deg,#0f2a4e 0%,#2f77b6 45%,#8fd2ef 70%,#163560 100%)}
.feature-panel{position:absolute;left:498px;top:0;width:478px;height:514px;border-radius:44px;background:linear-gradient(180deg,rgba(214,241,214,.96),rgba(200,240,196,.97))}
.feature-panel h2{position:absolute;left:36px;top:72px;font-size:34px;font-weight:500}
.feature-panel p{position:absolute;left:36px;width:418px;font-size:14px;line-height:25.6px;color:var(--grey);text-align:justify}

/* specialities */
.specialities{top:1859px;height:608px;background:linear-gradient(180deg,#d9f5d4,#c9efc3)}
.spec-text{left:114px;top:124px;font-size:17px;line-height:26px;width:480px}
.spec-item{position:absolute;display:flex;align-items:center;gap:22px;font-size:15.5px;font-weight:700}
.spec-icon{width:52px;height:52px;border-radius:8px;background:var(--green);display:flex;align-items:center;justify-content:center;box-shadow:0 2px 4px rgba(0,0,0,.15)}
.spec-photo{left:673px;top:79px;width:414px;height:344px;background:var(--green)}
.spec-photo div{position:absolute;left:18px;top:0;width:396px;height:344px;background:linear-gradient(135deg,#2a2520 0%,#6b4a2e 35%,#d89b52 55%,#3d4a55 75%,#161a1e 100%)}

/* founder */
.founder{top:2467px;height:688px;background:#fff}
.founder-intro{left:150px;top:80px;width:900px;text-align:center;font-size:16px;line-height:26px;color:#333}
.founder-back{left:138px;top:167px;width:350px;height:400px;border-radius:22px;background:var(--green)}
.founder-photo{left:111px;top:194px;width:352px;height:396px;border-radius:16px;background:linear-gradient(160deg,#5a5a5a,#2e2e2e 60%,#1f1f24)}
.founder-name{left:581px;top:188px;font-size:34px;font-weight:500}
.founder-text{left:581px;width:506px;font-size:14px;line-height:25.6px;color:var(--grey);text-align:justify}

/* blog */
.blog{top:3155px;height:760px;background:var(--green-pale)}
.post{position:absolute;top:125px;width:471px}
.post-image{width:471px;height:303px;border-radius:16px}
.post-title{position:absolute;left:35px;top:333px;font-size:21px;font-weight:700}
.post-text{position:absolute;left:35px;top:392px;width:405px;font-size:14px;line-height:23px;color:var(--grey)}
.post-more{position:absolute;left:35px;top:468px;font-size:13px;font-weight:700;text-decoration:underline;display:flex;align-items:center;gap:8px;color:var(--ink)}
.post-more .arrow{width:13px;height:13px;border-radius:50%;background:var(--ink);display:inline-flex;align-items:center;justify-content:center}

/* footer */
.footer{top:3860px;height:412px;background:var(--footer);color:#fff}
.footer-head{font-size:15px;font-weight:700;text-transform:uppercase;letter-spacing:.3px}
.field{position:absolute;background:#fff;border:1px solid #ccc;font-size:14px;color:#555;padding:11px 8px}
.submit{position:absolute;left:111px;top:323px;width:117px;height:44px;border-radius:22px;background:var(--green);color:var(--ink-btn);font-weight:700;font-size:15px;display:flex;align-items:center;justify-content:center}
.info-row{position:absolute;left:628px;display:flex;align-items:flex-start;gap:20px;font-size:14px;line-height:25px}
.info-icon{width:28px;height:28px;border-radius:50%;background:#5d7a5b;display:flex;align-items:center;justify-content:center;flex:none}
.quick{left:953px;top:128px}
.quick li{list-style:none;font-size:14px;height:34.5px;display:flex;gap:14px;align-items:flex-start}
.social{position:absolute;left:819px;top:304px;display:flex;gap:9px}
.social span{width:28px;height:28px;border-radius:50%;background:var(--green)}
.bottom-bar{top:4272px;height:54px;background:var(--green);font-size:14px;color:var(--ink)}
</style>
</head>
<body>
<div class="page">

  <!-- Header -->
  <header class="section site-header">
    <div class="abs brand">Zentraly</div>
    <div class="abs top-contact" style="left:658px">
      <span class="contact-icon"><svg width="12" height="9" viewBox="0 0 12 9"><rect x="0.5" y="0.5" width="11" height="8" fill="#fff"/><path d="M0.5 0.5L6 5l5.5-4.5" stroke="#000" fill="none"/></svg></span>
      <span>info@zentraly.net</span>
    </div>
    <div class="abs" style="left:873px;top:18px;width:1.5px;height:16px;background:#fff"></div>
    <div class="abs top-contact" style="left:918px;font-weight:700">
      <span class="contact-icon"><svg width="12" height="12" viewBox="0 0 24 24"><path d="M6.6 10.8a15 15 0 006.6 6.6l2.2-2.2c.3-.3.7-.4 1-.2 1.1.4 2.3.6 3.6.6.6 0 1 .4 1 1V20c0 .6-.4 1-1 1A17 17 0 013 4c0-.6.4-1 1-1h3.5c.6 0 1 .4 1 1 0 1.3.2 2.5.6 3.6.1.3 0 .7-.2 1z" fill="#fff"/></svg></span>
      <span>+1 555-014-7720</span>
    </div>
    <nav class="abs nav" style="left:0;width:1200px;height:20px">
      <a style="left:589px">Home</a>
      <a style="left:680px">About Us</a>
      <a style="left:794px">Our Services</a>
      <a style="left:932px">Blog</a>
      <a style="left:1013px">Contact us</a>
    </nav>
    <div class="abs" style="left:578px;top:88px;width:66px;height:2px;background:#fff"></div>
  </header>

  <!-- Hero -->
  <section class="section hero" role="img" aria-label="Silhouette of a person holding a tablet in front of a night city skyline">
    <h1 class="abs hero-title">AV Experts in Experiential Design</h1>
    <p class="abs hero-sub">Creating authentic immersive experiences by connecting the dots between people, spaces, and technology.</p>
    <div class="btn" style="left:111px;top:355px;width:174px">Get Started <span class="arrow"><svg width="7" height="7" viewBox="0 0 8 8"><path d="M2 1l3 3-3 3" stroke="#80de7c" stroke-width="1.8" fill="none"/></svg></span></div>
    <div class="abs hero-dots"><span></span><span></span><span class="off"></span><span></span><span></span></div>
  </section>

  <!-- Services overview -->
  <section class="section services">
    <h2 class="abs h2 center" style="top:40px">Our Services</h2>

    <article class="service-card" style="left:104px">
      <svg width="58" height="58" viewBox="0 0 58 58"><rect x="12" y="6" width="34" height="46" rx="3" fill="#4cc248"/><rect x="22" y="2" width="14" height="7" rx="2" fill="#2e8f2b"/><path d="M17 17l3 3 5-5M17 29l3 3 5-5M17 41l3 3 5-5" stroke="#fff" stroke-width="2.5" fill="none"/><path d="M29 18h11M29 30h11M29 42h6" stroke="#fff" stroke-width="2.5"/><circle cx="45" cy="44" r="8" fill="#2e8f2b"/><path d="M45 40v4h3" stroke="#fff" stroke-width="2" fill="none"/></svg>
      <div class="service-title">Planning &amp; Ideation</div>
      <div class="service-rule"></div>
      <p class="service-text">Our team will partner with you to determine if a concept is valid and that the equipment</p>
    </article>

    <article class="service-card" style="left:357px">
      <svg width="58" height="58" viewBox="0 0 58 58"><circle cx="29" cy="33" r="19" fill="none" stroke="#4cc248" stroke-width="8" stroke-dasharray="7 3"/><path d="M14 20a15 15 0 0130 0z" fill="#4cc248"/><rect x="11" y="19" width="36" height="5" rx="2" fill="#2e8f2b"/><circle cx="29" cy="35" r="7" fill="#4cc248"/></svg>
      <div class="service-title">Design Engineering</div>
      <div class="service-rule"></div>
      <p class="service-text">We will partner with you to provide independent design &amp; engineering services customized</p>
    </article>

    <article class="service-card" style="left:609px">
      <svg width="58" height="58" viewBox="0 0 58 58"><rect x="10" y="8" width="38" height="42" rx="2" fill="#4cc248"/><path d="M10 17h38M10 26h38M10 35h38M10 44h38M24 17v33" stroke="#fff" stroke-width="2.5"/><rect x="14" y="20" width="7" height="3" fill="#fff"/><rect x="14" y="29" width="7" height="3" fill="#fff"/></svg>
      <div class="service-title">Content Creation</div>
      <div class="service-rule"></div>
      <p class="service-text">The Zentraly Group is ready to create compelling content for you. The team has written</p>
    </article>

    <article class="service-card" style="left:862px">
      <svg width="58" height="58" viewBox="0 0 58 58"><rect x="12" y="8" width="34" height="44" rx="3" fill="#4cc248"/><rect x="22" y="4" width="14" height="8" rx="2" fill="#2e8f2b"/><path d="M17 20l2.5 2.5 4-4M17 31l2.5 2.5 4-4M17 42l2.5 2.5 4-4" stroke="#fff" stroke-width="2.3" fill="none"/><path d="M28 21h12M28 32h12M28 43h12" stroke="#fff" stroke-width="2.5"/></svg>
      <div class="service-title">Bid Preparation</div>
      <div class="service-rule"></div>
      <p class="service-text">Bid preparation can be a daunting task – for both integrators and stakeholders.</p>
    </article>
  </section>

  <!-- Hero-to-services zigzag -->
  <svg class="abs" style="left:0;top:640px" width="1200" height="110" viewBox="0 640 1200 110" aria-hidden="true">
    <polygon points="0,646 159,713 319,651 599,738 940,654 1040,713 1200,646 1200,750 0,750" fill="#b7e4b2"/>
    <polyline points="0,646 159,713 319,651 599,738 940,654 1040,713 1200,646" fill="none" stroke="#80de7c" stroke-width="5"/>
  </svg>

  <!-- Feature -->
  <section class="section feature">
    <div class="abs feature-block" role="img" aria-label="Businessman facing a glowing network of connected people over a city skyline">
      <div class="feature-panel">
        <h2>Our Services</h2>
        <p style="top:126px">Zentraly helps create authentic immersive experiences by connecting the dots between people, spaces, and technology. Physical spaces can be permanent, semi-permanent, or entirely temporary.</p>
        <p style="top:253px">Our mastery in audio, video, lighting, and control, combined with a deep understanding of how people interact with a space, enables Zentraly to create the ultimate connection between humans and technology infrastructure.</p>
        <div class="btn" style="left:36px;top:384px;width:176px">Learn More <span class="arrow"><svg width="7" height="7" viewBox="0 0 8 8"><path d="M2 1l3 3-3 3" stroke="#80de7c" stroke-width="1.8" fill="none"/></svg></span></div>
      </div>
    </div>
  </section>

  <!-- Specialities -->
  <section class="section specialities">
    <h2 class="abs h2" style="left:114px;top:64px">Our Specialities</h2>
    <p class="abs spec-text">View the wide range of services Zentraly offers our clients based on a variety of needs</p>

    <div class="spec-item" style="left:114px;top:204px">
      <span class="spec-icon"><svg width="26" height="28" viewBox="0 0 26 28"><path d="M3 2h13l5 5v19H3z" fill="#16361a"/><circle cx="18" cy="20" r="6" fill="#80de7c" stroke="#16361a" stroke-width="2"/><path d="M15.5 20l2 2 3-3.5" stroke="#16361a" stroke-width="1.8" fill="none"/></svg></span>Acceptance Testing
    </div>
    <div class="spec-item" style="left:364px;top:204px">
      <span class="spec-icon"><svg width="24" height="28" viewBox="0 0 24 28"><rect x="2" y="4" width="20" height="23" rx="2" fill="#16361a"/><rect x="7" y="1" width="10" height="6" rx="1.5" fill="#16361a" stroke="#80de7c"/><path d="M6 12h12M6 17h12M6 22h8" stroke="#80de7c" stroke-width="2"/></svg></span>Application Evaluation
    </div>
    <div class="spec-item" style="left:114px;top:283px">
      <span class="spec-icon"><svg width="24" height="28" viewBox="0 0 24 28"><rect x="6" y="1" width="16" height="22" rx="1" fill="#16361a"/><rect x="2" y="5" width="16" height="22" rx="1" fill="#16361a" stroke="#80de7c"/><path d="M5 11h10M5 15h10M5 19h10" stroke="#80de7c" stroke-width="1.6"/></svg></span>Content Creation
    </div>
    <div class="spec-item" style="left:364px;top:283px">
      <span class="spec-icon"><svg width="28" height="28" viewBox="0 0 28 28"><circle cx="14" cy="5" r="3.5" fill="#16361a"/><path d="M8 18l6-8 6 8" stroke="#16361a" stroke-width="3" fill="none"/><path d="M2 22c4 4 20 4 24 0" stroke="#16361a" stroke-width="3" fill="none"/></svg></span>14+ more services
    </div>

    <div class="btn" style="left:114px;top:381px;width:175px">Learn More <span class="arrow"><svg width="7" height="7" viewBox="0 0 8 8"><path d="M2 1l3 3-3 3" stroke="#80de7c" stroke-width="1.8" fill="none"/></svg></span></div>

    <div class="abs spec-photo"><div role="img" aria-label="Audio editing workstation with microphone and waveform monitors in warm light"></div></div>

    <svg class="abs" style="left:0;top:490px" width="1200" height="118" viewBox="0 2349 1200 118" aria-hidden="true">
      <polygon points="0,2372 160,2430 320,2370 600,2402 825,2368 1092,2462 1200,2385 1200,2470 0,2470" fill="#fff"/>
      <polyline points="0,2372 160,2430 320,2370 600,2402 825,2368 1092,2462 1200,2385" fill="none" stroke="#80de7c" stroke-width="5"/>
    </svg>
  </section>

  <!-- Founder -->
  <section class="section founder">
    <h2 class="abs h2 center" style="top:22px">Meet Our Founder</h2>
    <p class="abs founder-intro">Martin Hale has been involved in Audio, Video, Control, and Lighting design and installation for over 25 years. His projects stretch from conference rooms to stadiums and from hockey arenas to theme parks.</p>
    <div class="abs founder-back"></div>
    <div class="abs founder-photo" role="img" aria-label="Portrait photo of the founder in a dark jacket"></div>
    <h3 class="abs founder-name">Martin Hale</h3>
    <p class="abs founder-text" style="top:231px">Martin Hale has been involved in Audio, Video, Control, and Lighting design and installation for over 25 years. His comprehensive range of projects stretches from conference rooms to stadiums and from hockey arenas to theme parks. Martin’s roles in the industry have included integrator, manufacturer, and now end-user or owner’s representative. He was responsible for the Theme Park vertical market while employed by Corvell Audio Professional Systems.</p>
    <p class="abs founder-text" style="top:436px">After leaving Corvell Audio, Martin joined Parkline Creative as a Manager for Audio, Video, Lighting, and Projection to design the future of fun and next-generation experiences.</p>
    <div class="btn" style="left:581px;top:527px;width:176px">Learn More <span class="arrow"><svg width="7" height="7" viewBox="0 0 8 8"><path d="M2 1l3 3-3 3" stroke="#80de7c" stroke-width="1.8" fill="none"/></svg></span></div>
  </section>

  <!-- Blog -->
  <section class="section blog">
    <h2 class="abs h2 center" style="top:52px">Want to hear our thoughts?</h2>

    <article class="post" style="left:111px">
      <div class="post-image" role="img" aria-label="Team meeting around a table with laptops in a bright office" style="background:linear-gradient(135deg,#e9ece8 0%,#b9b4ab 40%,#5f5a55 70%,#d7dbd6 100%)"></div>
      <h3 class="post-title">The Ideation Process is Powerful</h3>
      <p class="post-text">This blog post walk through the process of ideation and how it can be applied to various problems. This specific problem was how to keep multiple calendars synchronized</p>
      <a class="post-more">READ MORE <span class="arrow"><svg width="6" height="6" viewBox="0 0 8 8"><path d="M2 1l3 3-3 3" stroke="#fff" stroke-width="2" fill="none"/></svg></span></a>
    </article>

    <article class="post" style="left:617px">
      <div class="post-image" role="img" aria-label="Three colleagues reviewing a document together at a desk" style="background:linear-gradient(135deg,#dfe3e3 0%,#9a9890 35%,#3f3c3a 65%,#c8c6c0 100%)"></div>
      <h3 class="post-title">Hello World!</h3>
      <p class="post-text">I have decided to launch my newest endeavor today, Friday, November 13, 2020 at 13:13 Eastern Standard Time. I was told on July 27 that the project</p>
      <a class="post-more">READ MORE <span class="arrow"><svg width="6" height="6" viewBox="0 0 8 8"><path d="M2 1l3 3-3 3" stroke="#fff" stroke-width="2" fill="none"/></svg></span></a>
    </article>
  </section>

  <!-- Footer zigzag -->
  <svg class="abs" style="left:0;top:3800px" width="1200" height="70" viewBox="0 3800 1200 70" aria-hidden="true">
    <polygon points="0,3860 168,3812 403,3893 599,3822 789,3893 1040,3812 1200,3860 1200,3870 0,3870" fill="#1c1c1c"/>
    <polyline points="0,3860 168,3812 403,3893 599,3822 789,3893 1040,3812 1200,3860" fill="none" stroke="#80de7c" stroke-width="5"/>
  </svg>

  <!-- Footer -->
  <footer class="section footer">
    <h4 class="abs footer-head" style="left:111px;top:94px">Get in Touch</h4>
    <div class="field" style="left:111px;top:134px;width:223px;height:43px">Name</div>
    <div class="field" style="left:344px;top:134px;width:223px;height:43px">Phone</div>
    <div class="field" style="left:111px;top:186px;width:456px;height:44px">Email</div>
    <div class="field" style="left:111px;top:236px;width:456px;height:77px;padding-top:8px">Message</div>
    <div class="submit">SUBMIT</div>

    <h4 class="abs footer-head" style="left:628px;top:97px;font-size:13.5px">Contact Info</h4>
    <div class="info-row" style="top:130px">
      <span class="info-icon"><svg width="12" height="15" viewBox="0 0 12 16"><path d="M6 0a6 6 0 00-6 6c0 4.5 6 10 6 10s6-5.5 6-10a6 6 0 00-6-6z" fill="#9fe39b"/><circle cx="6" cy="6" r="2.2" fill="#5d7a5b"/></svg></span>
      <span style="width:230px">2870 Lakeview Crossing Suite 210 – PMB42 Cedar Falls, FL 34010</span>
    </div>
    <div class="info-row" style="top:192px;font-weight:700;font-size:15px">
      <span class="info-icon"><svg width="13" height="13" viewBox="0 0 24 24"><path d="M6.6 10.8a15 15 0 006.6 6.6l2.2-2.2c.3-.3.7-.4 1-.2 1.1.4 2.3.6 3.6.6.6 0 1 .4 1 1V20c0 .6-.4 1-1 1A17 17 0 013 4c0-.6.4-1 1-1h3.5c.6 0 1 .4 1 1 0 1.3.2 2.5.6 3.6.1.3 0 .7-.2 1z" fill="#9fe39b"/></svg></span>
      <span>+1 555-014-7720</span>
    </div>
    <div class="info-row" style="top:244px">
      <span class="info-icon"><svg width="13" height="10" viewBox="0 0 12 9"><rect x="0.5" y="0.5" width="11" height="8" fill="#9fe39b"/><path d="M0.5 0.5L6 5l5.5-4.5" stroke="#5d7a5b" fill="none"/></svg></span>
      <span>info@zentraly.net</span>
    </div>
    <h4 class="abs footer-head" style="left:628px;top:309px;font-size:15.5px">Stay Connected</h4>
    <div class="social" aria-label="Social links"><span></span><span></span><span></span><span></span><span></span></div>

    <h4 class="abs footer-head" style="left:953px;top:97px;font-size:13.5px">Quick Links</h4>
    <ul class="abs quick">
      <li><span>»</span>Home</li>
      <li><span>»</span>About Us</li>
      <li><span>»</span>Our Services</li>
      <li><span>»</span>Latest Blog</li>
      <li><span>»</span>Contact Us</li>
    </ul>
  </footer>

  <div class="section bottom-bar">
    <div class="abs" style="left:111px;top:17px">© 2022 Zentraly. All Rights reserved</div>
    <div class="abs" style="left:908px;top:17px">Terms Of Use &nbsp;|&nbsp; Privacy Policy</div>
  </div>

</div>
</body>
</html>
```